PowerPoint Design Project for lernWyz

lernWyz is an online educational platform - founded by professors at Harrowgate Pell University and funded by the global manufacturing conglomerate TRV Holdings, Inc - that offers undergraduate and graduate level courses in business and engineering from professors at the world's top universities to interested learners worldwide.
lernWyz is launching a distance learning program and is looking to partner with schools/universities in different geographic locations for this purpose.
We need a PowerPoint presentation that will be circulated to the prospective schools that we would like to partner with.
Please find attached a PowerPoint presentation that we have prepared for this purpose. We would like these slides to look more professional and business-like, while adhering to their current content. In other words, we would like to see the same presentation but in the new style.
We would also like to use the template that you provide to prepare other presentation slides in the future.

Target Market(s)

Schools and universities worldwide

Industry/Entity Type

Business

Requirements
Must have
• Please find attached a PowerPoint presentation that we have prepared for this project. We would like these slides to look more professional and business-like, while adhering to their current content. In other words, we would like to see the SAME presentation but in the new style.

```html
<!DOCTYPE html>
<html lang="en">
<head>
<meta charset="utf-8">
<title>Sample Design and Redesign Decks – lernWyz</title>
<link href="https://fonts.googleapis.com/css2?family=Carlito&family=Lato:wght@400;700&display=swap" rel="stylesheet">
<style>
:root{
  --page:#d9d9d9;
  --slide:#ffffff;
  --navy:#1c2f6b;
  --steel:#3d5a8f;
  --brand-blue:#2c4f8f;
  --brand-green:#2f8a67;
  --ink:#333333;
  --muted:#6e6e6e;
  --link:#c2185b;
  --screen-cyan:#8ee3ea;
  --screen-grey:#b7c7c4;
  --frame:#1f3c7a;
}
*{box-sizing:border-box;margin:0;padding:0}
html,body{width:1200px;height:900px;overflow:hidden}
body{background:var(--page);font-family:"Lato",Arial,sans-serif;color:var(--ink);position:relative}
.page-title{position:absolute;top:36px;left:0;width:1200px;text-align:center;font-family:"Carlito",Calibri,sans-serif;font-size:27px;color:#111}
.slide{position:absolute;width:337px;height:252px;background:var(--slide);overflow:hidden}
.slide svg.band{position:absolute;left:0;top:0}
.brand{display:flex;align-items:center;gap:5px;color:var(--brand-blue);font-weight:400}
.brand .mark{width:14px;height:14px;border:2px solid var(--brand-blue);border-radius:2px}
.brand-lg{font-size:17px;justify-content:center}
.brand-lg .mark{width:18px;height:18px}
.sponsor{color:var(--brand-green);font-weight:700;font-size:16px;text-align:center}
.foot-brand{position:absolute;right:10px;bottom:8px;font-size:8px}
.foot-brand .mark{width:9px;height:9px;border-width:1.5px}
.foot-sponsor{position:absolute;left:12px;bottom:7px;font-size:10px}
.center-stack{position:absolute;left:0;right:0;text-align:center}
.deck-title{font-size:11.5px;line-height:1.2;color:#222}
.deck-date{font-size:6.5px;color:var(--muted);margin-top:4px}
.heading{position:absolute;left:22px;top:32px;font-size:13px;font-weight:700;color:#333}
.bullets{position:absolute;left:22px;right:22px;top:58px;list-style:none;font-size:7.6px;line-height:1.25;color:#444}
.bullets li{position:relative;padding-left:10px;margin-bottom:4px}
.bullets li::before{content:"•";position:absolute;left:0}
.bullets .sub{padding-left:10px;margin-bottom:0}
.bullets .sub::before{content:""}
.bullets a{color:var(--link)}
.platform-head{position:absolute;top:17px;left:0;right:0;display:flex;justify-content:center;align-items:center;gap:6px;font-size:6px;letter-spacing:.6px;color:#555}
.platform-head b{color:#222}
.platform-head .dot{width:12px;height:12px;border-radius:50%;background:#556}
.screen{position:absolute}
.caption{position:absolute;left:0;right:0;text-align:center;font-size:7.5px;color:#222}
.caption a{display:block;color:var(--link);font-size:6px;margin-top:3px}
.lab-title{position:absolute;top:52px;left:0;right:0;text-align:center;font-size:9px;font-weight:700;color:var(--navy)}
.lab-note{position:absolute;left:26px;right:40px;top:164px;font-size:6.8px;line-height:1.3;color:#444;padding-left:9px}
.lab-note::before{content:"•";position:absolute;left:0}
.badge{position:absolute;left:12px;bottom:7px;width:34px;height:10px;background:var(--frame);border-radius:2px}
</style>
</head>
<body>
<h1 class="page-title">Sample Design and Redesign Decks</h1>

<!-- Title slide -->
<section class="slide" style="left:34px;top:90px">
  <svg class="band" width="337" height="252" viewBox="0 0 337 252"><path d="M44 0 H64 C78 90 62 190 12 252 H0 V236 C34 180 52 100 44 0Z" fill="var(--navy)"/></svg>
  <div class="center-stack" style="top:60px"><div class="brand brand-lg"><span class="mark"></span>lernWyz</div></div>
  <div class="center-stack sponsor" style="top:110px">trv</div>
  <div class="center-stack" style="top:162px"><p class="deck-title">A TRV Holdings Sponsored Online Distance<br>Learning Program</p><p class="deck-date">November 8, 2013</p></div>
</section>

<!-- MOOCs slide -->
<section class="slide" style="left:424px;top:90px">
  <svg class="band" width="30" height="30" viewBox="0 0 30 30"><path d="M7 0 C9 9 6 16 0 20" fill="none" stroke="var(--navy)" stroke-width="4"/></svg>
  <h2 class="heading">MOOCs and Distance Learning</h2>
  <ul class="bullets">
    <li>Distance learning has traditionally been served by for-profit institutions that exclusively address off-campus students</li>
    <li>MOOCs are expected to disrupt the distance learning industry through the superior academic rankings of the member institutions</li>
    <li>Developing countries – like India – offer perhaps the largest student base for MOOC distance learning initiatives:</li>
    <li class="sub">i) Large, talented student body</li>
    <li class="sub">ii) Insufficient supply of spots in top Indian, US/European schools</li>
    <li class="sub">iii) Increasing demand for internationally recognized school credentials</li>
    <li class="sub">iv) US/European satellite campuses in India may take years to launch</li>
  </ul>
  <div class="brand foot-brand"><span class="mark"></span>lernWyz</div>
</section>

<!-- Sponsor profile slide -->
<section class="slide" style="left:813px;top:90px">
  <svg class="band" width="30" height="30" viewBox="0 0 30 30"><path d="M7 0 C9 9 6 16 0 20" fill="none" stroke="var(--navy)" stroke-width="4"/></svg>
  <h2 class="heading">TRV Holdings, Inc</h2>
  <ul class="bullets" style="font-size:7.2px">
    <li>TRV Holdings (<a>www.trv-holdings.example</a>) is a billion-dollar global manufacturing conglomerate with operating companies spanning the U.S., Europe, India, and China</li>
    <li>It is a world leader in several manufacturing areas, recognized by the United States Congress alongside companies like Northway Motors and Halden &amp; Brooks</li>
    <li>As a global employer of an educated workforce, TRV Holdings has undertaken a social mission to support higher education in developing countries</li>
    <li>Through lernWyz, TRV Holdings aims to democratize higher education in disciplines that have a real impact on people's daily lives, rendering transparent and usable the results of decades of university research to enhance their job readiness</li>
    <li>TRV Holdings has had a long standing interest in supporting education, offering scholarships and financial grants to college-bound children and educational institutions through a philanthropic Foundation</li>
  </ul>
  <div class="sponsor foot-sponsor">trv</div>
  <div class="brand foot-brand"><span class="mark"></span>lernWyz</div>
</section>

<!-- Platform slide -->
<section class="slide" style="left:34px;top:357px">
  <svg class="band" width="30" height="30" viewBox="0 0 30 30"><path d="M7 0 C9 9 6 16 0 20" fill="none" stroke="var(--navy)" stroke-width="4"/></svg>
  <div class="platform-head"><span class="dot"></span><span>THE SCHOLASTIC MARKET <b>SIMULATION PLATFORM</b></span></div>
  <div class="screen" role="img" aria-label="Screenshot of the SMSP platform home page" style="left:40px;top:38px;width:258px;height:170px;background:linear-gradient(90deg,var(--screen-cyan) 0 18%,var(--screen-grey) 18%);border:1px solid #999"></div>
  <p class="caption" style="top:214px">lernWyz's Business Platform: SMSP<a>http://www.scholastictrader.example</a></p>
  <div class="badge"></div>
  <div class="brand foot-brand"><span class="mark"></span>lernWyz</div>
</section>

<!-- Section slide -->
<section class="slide" style="left:424px;top:357px">
  <svg class="band" width="337" height="252" viewBox="0 0 337 252"><path d="M40 0 H66 C80 90 64 190 14 252 H0 V230 C32 176 50 100 40 0Z" fill="var(--steel)"/></svg>
  <div class="center-stack" style="top:112px;left:60px"><p class="deck-title" style="font-size:12px;color:#444">lernWyz's Distance Learning Program</p><p class="deck-date" style="font-size:8.5px">A TRV Holdings Sponsored Initiative</p></div>
  <div class="sponsor foot-sponsor" style="left:70px;bottom:14px;font-size:14px">trv</div>
  <div class="brand foot-brand" style="right:26px;bottom:15px;font-size:12px"><span class="mark" style="width:13px;height:13px"></span>lernWyz</div>
</section>

<!-- Certificate slide -->
<section class="slide" style="left:813px;top:357px">
  <svg class="band" width="30" height="30" viewBox="0 0 30 30"><path d="M7 0 C9 9 6 16 0 20" fill="none" stroke="var(--navy)" stroke-width="4"/></svg>
  <div class="platform-head"><span class="dot"></span><span>THE SCHOLASTIC MARKET <b>SIMULATION PLATFORM</b></span></div>
  <div class="screen" role="img" aria-label="Certificate of completion awarded to a course participant, signed by the course instructor of Harrowgate Pell University" style="left:85px;top:42px;width:172px;height:158px;background:#f3f3f0;border:6px solid var(--frame)"></div>
  <p class="caption" style="top:212px;font-size:6.5px">Certification of Completion Offered by lernWyz's<br>Business Platform: SMSP</p>
  <div class="brand foot-brand"><span class="mark"></span>lernWyz</div>
</section>

<!-- Lab slide -->
<section class="slide" style="left:34px;top:622px">
  <svg class="band" width="30" height="30" viewBox="0 0 30 30"><path d="M7 0 C9 9 6 16 0 20" fill="none" stroke="var(--navy)" stroke-width="4"/></svg>
  <div class="platform-head"><span class="dot"></span><span>THE SCHOLASTIC MARKET <b>SIMULATION PLATFORM</b></span></div>
  <h2 class="lab-title">The Financial Trading Laboratory</h2>
  <div class="screen" role="img" aria-label="Screenshot of the trading laboratory portfolio page" style="left:24px;top:76px;width:142px;height:78px;background:linear-gradient(90deg,var(--screen-grey) 0 75%,var(--screen-cyan) 75%);border:1px solid #999"></div>
  <div class="screen" role="img" aria-label="Screenshot of the trading laboratory simulation chart page" style="left:174px;top:76px;width:142px;height:78px;background:linear-gradient(90deg,var(--screen-cyan) 0 20%,#e8eeee 20% 78%,var(--screen-cyan) 78%);border:1px solid #999"></div>
  <p class="lab-note">The online laboratory provides a rich experience to registered users, including the ability to easily track portfolio value, network with other SMSP users (using leading social media platforms), and save simulations for future reference.</p>
  <div class="brand foot-brand"><span class="mark"></span>lernWyz</div>
</section>

<!-- Closing slide -->
<section class="slide" style="left:424px;top:622px">
  <svg class="band" width="337" height="252" viewBox="0 0 337 252"><path d="M44 0 H60 C74 90 58 190 10 252 H0 V238 C32 182 50 100 44 0Z" fill="var(--navy)"/></svg>
  <div class="center-stack" style="top:62px"><div class="brand brand-lg"><span class="mark"></span>lernWyz</div></div>
  <div class="center-stack sponsor" style="top:112px">trv</div>
  <div class="center-stack" style="top:172px"><p class="deck-title" style="font-size:12px">Thank You</p><p class="deck-date">November 8, 2013</p></div>
</section>
</body>
</html>
```